- Redesign our business card
- Logo remains unchanged
- Current business card attached

Target Market(s)

We are a property management company

Industry/Entity Type

Business

```html
<!DOCTYPE html>
<html lang="en">
<head>
<meta charset="utf-8">
<title>Harlow Property Group – Business Card</title>
<link rel="stylesheet" href="https://fonts.googleapis.com/css2?family=Arimo:wght@400;700&display=swap">
<style>
  :root {
    --page: #ffffff;
    --card-edge: #3a3a3a;
    --khaki: #bdb867;
    --khaki-deep: #b3ad5c;
    --khaki-light: #f6f4df;
    --brand-ink: #3d3d1c;
    --brand-mark: #6c6b3b;
    --ink-light: #ffffff;
    --band-text: #cfcb93;
  }
  * { margin: 0; padding: 0; box-sizing: border-box; }
  html, body {
    width: 965px;
    height: 1200px;
    overflow: hidden;
    background: var(--page);
    font-family: "Arimo", Arial, sans-serif;
  }
  .sheet { position: relative; width: 965px; height: 1200px; }

  .card {
    position: absolute;
    left: 4px;
    width: 957px;
    height: 576px;
    border: 1.5px solid var(--card-edge);
    overflow: hidden;
  }

  /* Front */
  .card--front {
    top: 4px;
    background: radial-gradient(ellipse 62% 58% at 48% 56%, var(--khaki-light) 0%, #e2dfae 35%, var(--khaki) 75%, var(--khaki-deep) 100%);
  }
  .brand {
    position: absolute;
    left: 89px;
    top: 400px;
    display: flex;
    align-items: center;
    gap: 18px;
  }
  .brand__mark {
    width: 34px;
    height: 34px;
    background: var(--brand-mark);
  }
  .brand__name {
    font-size: 38px;
    font-weight: 700;
    letter-spacing: 1px;
    color: var(--brand-ink);
  }
  .brand__services {
    position: absolute;
    left: 141px;
    top: 458px;
    font-size: 27px;
    font-weight: 700;
    letter-spacing: 1px;
    color: var(--brand-ink);
  }

  /* Back */
  .card--back {
    top: 617px;
    background: var(--khaki);
    color: var(--ink-light);
  }
  .accent-rule {
    position: absolute;
    left: 0;
    top: 96px;
    width: 563px;
    height: 4px;
    background: var(--ink-light);
  }
  .person { position: absolute; left: 32px; top: 104px; }
  .person__name { font-size: 33px; font-weight: 700; line-height: 1.1; }
  .person__role { font-size: 26px; line-height: 1.1; }

  .addresses {
    position: absolute;
    left: 0;
    top: 270px;
    width: 1000px;
    text-align: center;
    font-size: 22.5px;
    font-weight: 700;
    line-height: 27px;
  }

  .online {
    position: absolute;
    left: 32px;
    top: 452px;
    font-size: 24px;
    line-height: 23px;
  }
  .online__web { display: block; padding-left: 38px; }

  .phones {
    position: absolute;
    left: 714px;
    top: 421px;
    font-size: 24px;
    line-height: 25.5px;
  }
  .phones__row { display: block; white-space: nowrap; }
  .phones__label { display: inline-block; width: 38px; text-align: right; }

  .services-band {
    position: absolute;
    left: 0;
    bottom: 0;
    width: 100%;
    height: 55px;
    background: var(--page);
    border-top: 3px solid var(--khaki);
    padding-left: 32px;
    display: flex;
    align-items: center;
    font-size: 24px;
    color: var(--band-text);
    white-space: nowrap;
  }
  .services-band__sep { padding: 0 14px; }
</style>
</head>
<body>
<div class="sheet">

  <section class="card card--front" aria-label="Card front">
    <div class="brand">
      <span class="brand__mark" aria-hidden="true"></span>
      <span class="brand__name">HARLOW PROPERTY GROUP</span>
    </div>
    <p class="brand__services">STRATA MANAGEMENT SERVICES</p>
  </section>

  <section class="card card--back" aria-label="Card back">
    <div class="accent-rule"></div>
    <div class="person">
      <h1 class="person__name">NATHANIEL HARLOW</h1>
      <p class="person__role">Licensed Strata Manager</p>
    </div>

    <address class="addresses" style="font-style: normal;">
      PO BOX 48, ELMWOOD HILLS NSW 2099<br>
      12/6-20 ASHCROFT STREET ELMWOOD NSW 2098
    </address>

    <p class="online">
      E: info@harlowproperty.com.au
      <span class="online__web">www.harlowproperty.com.au</span>
    </p>

    <p class="phones">
      <span class="phones__row"><span class="phones__label">F:</span> 02 9000 4815</span>
      <span class="phones__row"><span class="phones__label">T:</span> 02 9000 0372</span>
      <span class="phones__row"><span class="phones__label">M:</span> 0400 555 218</span>
    </p>

    <div class="services-band">
      <span>Strata Management</span>
      <span class="services-band__sep">I</span>
      <span>Community Management</span>
      <span class="services-band__sep">I</span>
      <span>Property Management</span>
    </div>
  </section>

</div>
</body>
</html>
```